Business Card Design Project

Double-side business card.
Side One:
Logo (Including the word TOLVEKA that is part of the Logo
"Programas de Renovación Urbana y Cuidado del Entorno Natural Andino"
Side Two:
Marcela Ostrander
Co-Founder & CEO
Washington, DC (USA)
email: marcelao@tolveka.example (please use an icon for "emal")
cell: +1 (202) 555 0147 (please use an icon for "cell")
skype: marceostrander (please use an icon for "skype")
twitter: marceostrander (please use an icon for "twitter")
www.tolveka.example
Target Market(s)
Foundations, Governments, and Private sector companies that implement projects for sustainability.
Industry/Entity Type
Business
Font styles to use
Colors
Designer to choose colors to be used in the design.
Requirements
Nice to have
- barcode

```html
<!DOCTYPE html>
<html lang="es">
<head>
<meta charset="utf-8">
<title>TOLVEKA — Business Card</title>
<link href="https://fonts.googleapis.com/css2?family=PT+Sans+Narrow:wght@400;700&display=swap" rel="stylesheet">
<style>
  :root {
    --page-bg: #2b3547;
    --card-light: #f4f4f4;
    --card-mid: #dedede;
    --ink-dark: #3b3b3b;
    --ink-grey: #7a7a7a;
    --teal: #135f6e;
    --teal-text: #1c6274;
    --band-grey: #8f8f8f;
    --ring-grey: #d6d6d6;
    --bubble: #a9d3ea;
  }
  * { margin: 0; padding: 0; box-sizing: border-box; }
  html, body { width: 1200px; height: 970px; overflow: hidden; }
  body {
    background: var(--page-bg);
    font-family: "PT Sans Narrow", "Arial Narrow", sans-serif;
    position: relative;
  }
  .card {
    position: absolute;
    background:
      radial-gradient(ellipse 260px 160px at 22% 40%, #ffffff 0%, rgba(255,255,255,0) 100%),
      linear-gradient(180deg, var(--card-light) 0%, var(--card-mid) 100%);
    overflow: hidden;
  }
  .card--front { left: 93px; top: 53px; width: 694px; height: 416px; }
  .card--back { left: 395px; top: 488px; width: 723px; height: 432px; }

  .front-brand {
    position: absolute; left: 0; right: 0; top: 232px;
    text-align: center;
    font-size: 58px; font-weight: 400; letter-spacing: 6px;
    color: var(--ink-grey); line-height: 1;
  }
  .front-tagline {
    position: absolute; left: 0; right: 0; top: 298px;
    text-align: center;
    font-size: 16px; font-weight: 400; color: var(--teal-text);
  }

  .holder-name {
    position: absolute; left: 0; right: 0; top: 36px;
    text-align: center; font-size: 42px; font-weight: 700; line-height: 1;
    color: var(--ink-dark);
  }
  .holder-name .surname { color: var(--teal); }
  .holder-title {
    position: absolute; left: 0; right: 0; top: 94px;
    text-align: center; font-size: 21px; font-weight: 700; color: #444;
  }
  .divider-band { position: absolute; left: 0; top: 0; }
  .back-brand {
    position: absolute; left: 292px; top: 207px; width: 120px;
    text-align: center; font-size: 26px; font-weight: 400; letter-spacing: 1px;
    color: #ffffff; line-height: 1;
  }
  .contact { position: absolute; list-style: none; }
  .contact--left { left: 72px; top: 292px; }
  .contact--right { left: 506px; top: 292px; }
  .contact li {
    display: flex; align-items: center; height: 35.5px;
    font-size: 16px; color: #333;
  }
  .contact .icon { width: 24px; height: 24px; margin-right: 10px; flex: none; }
</style>
</head>
<body>

  <section class="card card--front" aria-label="Card front">
    <div class="front-brand">TOLVEKA</div>
    <p class="front-tagline">"Programas de Renovación Urbana y Cuidado del Entorno Natural Andino"</p>
  </section>

  <section class="card card--back" aria-label="Card back">
    <h1 class="holder-name">Marcela <span class="surname">Ostrander</span></h1>
    <p class="holder-title">Co-Founder &amp; CEO</p>

    <svg class="divider-band" width="723" height="300" viewBox="0 0 723 300" aria-hidden="true">
      <rect x="0" y="200" width="723" height="18" fill="var(--band-grey)"/>
      <rect x="0" y="221" width="723" height="4" fill="var(--teal)"/>
      <rect x="0" y="228" width="723" height="22" fill="var(--band-grey)"/>
      <circle cx="405" cy="177" r="28" fill="var(--bubble)" opacity="0.75"/>
      <circle cx="390" cy="157" r="14" fill="var(--bubble)" opacity="0.6"/>
      <circle cx="285" cy="257" r="30" fill="var(--bubble)" opacity="0.75"/>
      <circle cx="317" cy="287" r="13" fill="var(--bubble)" opacity="0.6"/>
      <circle cx="352" cy="218" r="74" fill="var(--ring-grey)"/>
      <circle cx="352" cy="218" r="66" fill="var(--teal)"/>
    </svg>
    <div class="back-brand">TOLVEKA</div>

    <ul class="contact contact--left">
      <li>
        <svg class="icon" viewBox="0 0 24 24" aria-hidden="true"><path d="M12 3 1 12h3v9h6v-6h4v6h6v-9h3z" fill="var(--teal)"/></svg>
        Washington, DC (USA)
      </li>
      <li>
        <svg class="icon" viewBox="0 0 24 24" aria-hidden="true"><circle cx="12" cy="12" r="8" fill="var(--teal)"/></svg>
        marceostrander
      </li>
      <li>
        <svg class="icon" viewBox="0 0 24 24" aria-hidden="true"><circle cx="12" cy="12" r="8" fill="var(--teal)"/></svg>
        marceostrander
      </li>
    </ul>

    <ul class="contact contact--right">
      <li>
        <svg class="icon" viewBox="0 0 24 24" aria-hidden="true"><rect x="7" y="2" width="10" height="20" rx="2" fill="none" stroke="var(--teal)" stroke-width="1.6"/><circle cx="12" cy="18.5" r="1" fill="var(--teal)"/></svg>
        +1 (202) 555 0147
      </li>
      <li>
        <svg class="icon" viewBox="0 0 24 24" aria-hidden="true"><rect x="5" y="7" width="14" height="10" fill="none" stroke="var(--teal)" stroke-width="1.4"/><path d="M5 7l7 6 7-6" fill="none" stroke="var(--teal)" stroke-width="1.4"/></svg>
        marcelao@tolveka.example
      </li>
      <li>
        <svg class="icon" viewBox="0 0 24 24" aria-hidden="true"><g fill="none" stroke="var(--teal)" stroke-width="1.4"><circle cx="12" cy="12" r="7"/><ellipse cx="12" cy="12" rx="3" ry="7"/><path d="M5 12h14"/></g></svg>
        www.tolveka.example
      </li>
    </ul>
  </section>

</body>
</html>
```